Cannabis Vape Cartridge Box. For HUGE Cannabis brand.

We need help with a product for our All-in-One Rosin Vape product. Our brand is called Yelvra, and we are based in New Mexico. The product is all natural so we want the design look like natural as well. We will be using a soft touch box, so we want the packaging to look how the box feels in the hands. The box feels soft and smooth. We do not want to use any cannabis leaves in the design. We are also interested in vibrational patterns. I have attached examples of packaging that we like as well as the template of our boxes we will be using and also our logos.
Updates
With all new designs- please put the word Rosin on the box.
Colors
Designer to choose colors to be used in the design.
Look and feel

```html
<!DOCTYPE html>
<html lang="en">
<head>
<meta charset="utf-8">
<title>Yelvra Rosin Vape Box</title>
<link rel="stylesheet" href="https://fonts.googleapis.com/css2?family=Roboto+Condensed:wght@400;700;900&display=swap">
<style>
  :root {
    --stage: #f3f2ef;
    --ink: #141414;
    --orange: #f29a2e;
    --amber: #f6c244;
    --blush: #eab1b6;
    --mauve: #c98ca9;
    --cream: #f7dcc6;
    --white: #ffffff;
    --warn: #d8363a;
  }
  * { box-sizing: border-box; margin: 0; padding: 0; }
  html, body { width: 1200px; height: 1180px; overflow: hidden; }
  body {
    background: var(--stage);
    font-family: "Roboto Condensed", "Arial Narrow", sans-serif;
    color: var(--ink);
    position: relative;
  }
  .panel {
    position: absolute;
    top: 80px;
    width: 250px;
    height: 1020px;
    overflow: hidden;
  }
  .panel--front { left: 330px; }
  .panel--back { left: 640px; }

  .marble { position: absolute; inset: 0; }
  .panel--front .marble {
    background:
      radial-gradient(ellipse 60% 30% at 70% 35%, var(--amber) 0%, transparent 70%),
      radial-gradient(ellipse 50% 25% at 30% 70%, var(--mauve) 0%, transparent 70%),
      radial-gradient(ellipse 60% 20% at 60% 90%, var(--blush) 0%, transparent 70%),
      linear-gradient(160deg, var(--cream) 0%, var(--orange) 35%, var(--amber) 55%, var(--mauve) 75%, var(--orange) 100%);
  }
  .panel--back .marble {
    background:
      radial-gradient(ellipse 50% 20% at 80% 10%, var(--orange) 0%, transparent 70%),
      radial-gradient(ellipse 60% 30% at 35% 45%, var(--blush) 0%, transparent 70%),
      radial-gradient(ellipse 40% 25% at 70% 75%, var(--amber) 0%, transparent 70%),
      linear-gradient(175deg, var(--orange) 0%, var(--cream) 25%, var(--blush) 50%, var(--cream) 70%, var(--mauve) 100%);
  }

  /* Front */
  .brand-disc {
    position: absolute;
    left: 20px;
    top: 120px;
    width: 224px;
    height: 224px;
    border-radius: 50%;
    background: radial-gradient(circle, #f0a24a 0%, #d9803a 60%, #b8602e 100%);
  }
  .brand-name {
    position: absolute;
    left: 8px;
    top: 128px;
    width: 110px;
    display: flex;
    flex-direction: column;
    align-items: center;
    font-weight: 900;
    font-size: 96px;
    line-height: 1;
    color: var(--ink);
  }
  .brand-name span { display: block; height: 112px; }
  .thc-mark { position: absolute; left: 170px; top: 782px; }
  .product-type {
    position: absolute; left: 0; width: 190px; top: 830px;
    text-align: center; font-weight: 700; font-size: 36px; letter-spacing: 0.5px;
  }
  .product-desc {
    position: absolute; left: 0; width: 190px; top: 897px;
    text-align: center; font-weight: 700; font-size: 19px; line-height: 1.05;
  }
  .product-size {
    position: absolute; left: 0; width: 190px; top: 965px;
    text-align: center; font-weight: 700; font-size: 19px;
  }

  /* Back */
  .info { position: absolute; left: 8px; top: 26px; width: 218px; font-size: 11px; line-height: 1.45; }
  .info-title { font-weight: 700; font-size: 17px; margin-bottom: 8px; }
  .info strong { font-weight: 700; }
  .ingredients { position: absolute; left: 8px; top: 400px; width: 200px; font-size: 12px; line-height: 1.45; }
  .ingredients-title { font-weight: 700; font-size: 17px; margin-bottom: 4px; }
  .note { font-weight: 700; font-size: 13px; margin-top: 28px; line-height: 1.5; }
  .solvents { font-size: 13px; margin-top: 24px; }
  .expiry { position: absolute; left: 8px; top: 816px; width: 130px; font-weight: 700; font-size: 13px; line-height: 1.5; }
  .rule { position: absolute; left: 8px; top: 872px; width: 140px; border-top: 1px solid var(--ink); }
  .usage { position: absolute; left: 8px; top: 894px; width: 140px; font-size: 13px; line-height: 1.5; }
  .usage p + p { margin-top: 20px; }
  .usage strong { font-weight: 700; }
</style>
</head>
<body>

<section class="panel panel--front" aria-label="Box front">
  <div class="marble" role="img" aria-label="Marbled fluid-art pattern in orange, yellow and pink"></div>
  <div class="brand-disc"></div>
  <h1 class="brand-name" aria-label="Yelvra">
    <span>Y</span><span>E</span><span>L</span><span>V</span><span>R</span><span>A</span>
  </h1>
  <svg class="thc-mark" width="70" height="110" viewBox="0 0 70 110" aria-hidden="true">
    <polygon points="35,3 67,55 35,107 3,55" fill="var(--white)" stroke="var(--warn)" stroke-width="3"/>
  </svg>
  <p class="product-type">ROSIN</p>
  <p class="product-desc">CAREFULLY BLENDED<br>DIPOSABLE VAPE</p>
  <p class="product-size">1 GRAM</p>
</section>

<section class="panel panel--back" aria-label="Box back">
  <div class="marble" role="img" aria-label="Marbled fluid-art pattern in pink, peach and orange"></div>
  <div class="info">
    <p class="info-title">MUST BE 21+ TO ENJOY</p>
    <p><strong>WARNING: For use by adults 21 and over.</strong> Keep out of reach of children. Do not drive or operate heavy machinery while under the influence of cannabis. BE CAUTIOUS a <strong>Cannabinoid edibles can take up to two hours or more to take effect.</strong> This product is not approved by the FDA to treat, cure, or prevent any disease. FDA has not evaluated this product for safety, effectiveness, and quality. There may be long term adverse health effects from consumption of cannabis, including additional risks for women who are or may become pregnant or are breastfeeding. For accidental ingestion: Call Poison Control 1-800-555-0142.</p>
  </div>
  <div class="ingredients">
    <p class="ingredients-title">Ingredients:</p>
    <p>Ethanol extracted Cannabis oil, natural terpenes</p>
    <p class="note">No pesticides used in the making of this product.</p>
    <p class="solvents"><strong>Solvents used:</strong> Ethanol</p>
  </div>
  <p class="expiry">Expires one year after manufacturing date.</p>
  <div class="rule"></div>
  <div class="usage">
    <p><strong>Intended use:</strong> Inhalant</p>
    <p><strong>DIRECTIONS:</strong> Press to lips and inhale</p>
  </div>
</section>

</body>
</html>
```